Glazmor signs for fridge and desk

I require 3 a4 designs very basic designs with single colour and easy to print. I have atached a style guide to see the fonts I used in my last three design. Please remember I'm printing in only one colour
PLease see the following link, of what I sell on zorblu. I will be selling this allong side these products.
https://www.zorblu.com/gp/item/K52QX8RMVA
Please see my competitors
https://www.zorblu.com/Memo-Sticky-Schedule-Cooler-Holder/it/K9TRW4HQDP/ref=sr_1_8?keywords=clear%2Bmemo%2Bpanel%2Bcooler%2Bwipe%2Bclean%2Bpanel%2Bsticky%2Bsee&qid=1600112233&sr=8-8&th=1
and
https://www.zorblu.com/Sticky-Clear-Schedule-Cooler-Chiller/it/K7MPQ2XTRD/ref=sr_1_4_sp?keywords=clear+memo+panel+cooler+wipe+clean+panel+sticky+see&qid=1600114455&sr=8-4-promo&psc=1&spLa=QmxhaGJsYWhibGFoYmxhaGJsYWhibGFoYmxhaGJsYWhibGFoYmxhaGJsYWhibGFoYmxhaGJsYWhibGFoYmxhaGJsYWhibGFoYmxhaGJsYWhibGFoYmxhaGJsYWhibGFoYmxhaGJsYWhibGFoYmxhaGJsYWhibGFoYmxhaGJsYWhibGFoYmxhaGJsYWhibGFoYmxhaGJsYWhibGFoYmxhaGJsYWg=
I'd like something more fun and different. But that can still be printed on Glazmor with one colour and be functional. A shopping list, a weekly planner(both that stick to a fridge) and a to do list that will sit on a desk or kitchen counter top.
PLease design
1st a4
Break into seven parts, with seven headings..... Monday to Sunday.... here customers will be able to write menus and upcoming events. I want this landcape
2nd a4
'Shopping List' is to be the heading
I want this landcape
3rd a4
'To Do List' is the only text I would like
I would like this portrat and lines marked and a check box on the left hand side
Remember I can only print on the acrylic with one colour. I want to be different from my competitors but I do want to be functional.
just a reminder. I can only print with one colour

```html
<!DOCTYPE html>
<html lang="en">
<head>
<meta charset="UTF-8">
<title>Glazmor Shopping List – Fridge Sign</title>
<link rel="stylesheet" href="https://fonts.googleapis.com/css2?family=Kaushan+Script&family=Montserrat:wght@500&display=swap">
<style>
  :root {
    --page-bg: #ffffff;
    --ink: #000000;
    --steel-dark: #8c8f93;
    --steel-mid: #b3b6ba;
    --steel-light: #d4d6d9;
  }
  html, body {
    margin: 0;
    padding: 0;
    overflow: hidden;
    background: var(--page-bg);
  }
  .sheet {
    position: relative;
    width: 839px;
    height: 1200px;
    background: var(--page-bg);
    overflow: hidden;
  }
  .fridge-photo {
    position: absolute;
    left: 170px;
    top: 90px;
    width: 507px;
    height: 512px;
    background: linear-gradient(to bottom,
      var(--steel-dark) 0%,
      var(--steel-mid) 45%,
      var(--steel-light) 70%,
      var(--page-bg) 100%);
    border-radius: 4px 4px 0 0;
  }
  .list-board {
    position: absolute;
    left: 90px;
    top: 619px;
    width: 661px;
    height: 462px;
    box-sizing: border-box;
    border: 2.5px solid var(--ink);
    border-radius: 13px;
  }
  .list-title {
    position: absolute;
    left: 0;
    right: 0;
    top: 3px;
    margin: 0;
    text-align: center;
    font-family: "Kaushan Script", cursive;
    font-weight: 400;
    font-size: 46px;
    line-height: 1.2;
    color: var(--ink);
    transform: translateX(-13px);
  }
  .title-rule {
    position: absolute;
    left: 11px;
    right: 13px;
    top: 69px;
    height: 0;
    border-top: 1.5px solid var(--ink);
  }
  .colour-note {
    position: absolute;
    left: 148px;
    top: 1112px;
    margin: 0;
    font-family: "Montserrat", sans-serif;
    font-weight: 500;
    font-size: 12px;
    letter-spacing: 0.1px;
    color: var(--ink);
    white-space: nowrap;
  }
</style>
</head>
<body>
  <main class="sheet">
    <div class="fridge-photo" role="img" aria-label="Photo of a stainless steel fridge with the Shopping List sign applied to the freezer door"></div>

    <section class="list-board">
      <h1 class="list-title">Shopping List</h1>
      <div class="title-rule"></div>
    </section>

    <p class="colour-note">THIS WILL BE WHITE COLOUR, , OR ANY COLOUR DEPENDING ON REQUIREMENT</p>
  </main>
</body>
</html>
```